We are looking for a poster / flyer to advertise our Squash Tournament - the Wrenfold Club Sydney CBD Squash Open. I have provided the details and sponsor logos that need to appear on the poster in the attachments.
I am open to the poster including pictures of real life squash playing action shots or a complete graphic art design.

Target Market(s)

Squash Players and Sporty People who may be interested in trying Squash as a new Sport

Requirements
Must have
• 1. All logos attached in files (logos in the word doc and the Bramwick Logo)
2. Content that has been provided in the word doc
3. Printable on A3 paper
4. Title of the poster must be 2021 Wrenfold Club Sydney CBD Squash Open
Nice to have
• 1.Design must be related to the Sport of Squash (can either be a graphic Design that incorporates a real life squash pic rom the internet or 100% graphic)
2. Something incorporating both female and junior squash player participation.
3. Poster depicts action / athleticism.

```html
<!DOCTYPE html>
<html lang="en">
<head>
<meta charset="utf-8">
<title>2021 Wrenfold Club Sydney CBD Squash Open</title>
<link rel="stylesheet" href="https://fonts.googleapis.com/css2?family=Roboto+Condensed:wght@300;400;700&display=swap">
<style>
  :root {
    --navy: #111d58;
    --red: #e31e26;
    --ink: #1c1c1c;
    --paper: #ffffff;
    --backdrop: #e4e4e4;
    --rule: #c9ccd6;
    --font: "Roboto Condensed", "Arial Narrow", sans-serif;
  }
  * { margin: 0; padding: 0; box-sizing: border-box; }
  html, body { width: 1200px; height: 1200px; overflow: hidden; background: var(--backdrop); }
  body { font-family: var(--font); color: var(--ink); }

  .poster {
    position: absolute; left: 172px; top: 0;
    width: 856px; height: 1200px;
    background: var(--paper);
  }
  .abs { position: absolute; }
  .center { left: 0; right: 0; text-align: center; }

  .brand { top: 40px; font-weight: 300; font-size: 46px; letter-spacing: 6px; color: var(--ink); }

  .title-top { top: 128px; font-size: 48px; font-weight: 400; color: var(--ink); letter-spacing: 0.5px; }
  .title-main { top: 180px; font-size: 55px; font-weight: 700; color: var(--red); letter-spacing: 0.5px; }

  .date-pill {
    left: 253px; top: 250px; width: 357px; height: 43px;
    background: var(--navy); border-radius: 22px;
    display: flex; align-items: center; justify-content: center; gap: 16px;
    color: #fff; font-size: 26px; font-weight: 300;
  }
  .date-pill sup { font-size: 14px; }

  .venue { top: 314px; font-size: 14px; line-height: 24px; color: var(--ink); }

  .hero {
    left: 112px; top: 373px; width: 632px; height: 530px;
    background: radial-gradient(ellipse at 50% 45%, #2b3fa8 0%, #1a2770 30%, #e3333a 55%, rgba(227,51,58,0.25) 72%, rgba(255,255,255,0) 85%);
  }

  .bar-tab {
    left: 212px; top: 710px; width: 410px; height: 68px;
    background: var(--paper);
    display: flex; align-items: center; gap: 6px; padding-left: 36px;
  }
  .bar-tab .amount { font-size: 52px; font-weight: 700; color: var(--red); }
  .bar-tab .label { writing-mode: vertical-rl; transform: rotate(180deg); font-size: 14px; color: var(--red); }
  .bar-tab .desc { font-size: 23px; line-height: 24px; color: var(--ink); margin-left: 6px; }

  .grades-box {
    left: 62px; top: 933px; width: 762px; height: 188px;
    border: 1.5px solid var(--rule); border-radius: 12px;
  }
  .grades-title {
    top: 913px; left: 0; right: 0; margin: 0 auto; width: 310px;
    background: var(--paper); text-align: center;
    font-size: 29px; font-weight: 700; color: var(--navy);
  }
  .grades-list { list-style: none; font-size: 18px; line-height: 23px; }
  .grades-list li { position: relative; padding-left: 22px; margin-bottom: 3px; }
  .grades-list li::before { content: "»"; position: absolute; left: 0; top: -2px; color: var(--red); font-size: 20px; }
  .grades-list strong { color: var(--navy); font-weight: 700; }
  .col-a { left: 134px; top: 960px; width: 240px; }
  .col-b { left: 449px; top: 960px; width: 320px; }

  .weekday { top: 1051px; font-size: 12px; }
  .entries { top: 1070px; font-size: 16px; }

  .contact {
    left: 120px; top: 1103px; width: 612px; height: 37px;
    display: flex; border-radius: 19px; overflow: hidden;
    border: 2px solid var(--navy); background: var(--navy);
  }
  .contact .director {
    width: 232px; background: var(--paper); border-radius: 0 19px 19px 0;
    display: flex; flex-direction: column; align-items: center; justify-content: center;
  }
  .director .name { font-size: 17px; font-weight: 700; color: var(--navy); line-height: 17px; }
  .director .role { font-size: 7px; color: var(--red); letter-spacing: 0.5px; }
  .contact .details { flex: 1; display: flex; align-items: center; color: #fff; font-size: 14px; padding-left: 22px; gap: 10px; }
  .details .divider { width: 1px; height: 18px; background: rgba(255,255,255,0.5); margin: 0 10px; }
  .details svg { flex: none; }

  .partners {
    left: 150px; top: 1150px; width: 560px; height: 40px;
    display: flex; align-items: center; justify-content: space-between;
  }
  .partner-name { font-size: 12px; font-weight: 700; color: var(--navy); }
  .partner-shape { width: 34px; height: 34px; border-radius: 50%; background: var(--navy); }
  .partner-shape.square { border-radius: 4px; background: #3a4aa0; }
</style>
</head>
<body>
<main class="poster">
  <div class="abs center brand">BRAMWICK</div>

  <h1 class="abs center title-top">2021 WRENFOLD CLUB</h1>
  <h2 class="abs center title-main">SYDNEY CBD SQUASH OPEN</h2>

  <div class="abs date-pill">
    <svg width="28" height="26" viewBox="0 0 28 26" fill="none" stroke="#fff" stroke-width="1.5">
      <rect x="2" y="4" width="24" height="20" rx="2"/>
      <line x1="2" y1="9" x2="26" y2="9"/>
      <line x1="8" y1="1" x2="8" y2="6"/><line x1="20" y1="1" x2="20" y2="6"/>
      <rect x="6" y="12" width="3" height="3"/><rect x="12" y="12" width="3" height="3"/><rect x="6" y="18" width="3" height="3"/>
      <polyline points="16,19 19,22 24,16"/>
    </svg>
    <span>13<sup>th</sup> – 15<sup>th</sup> AUGUST</span>
  </div>

  <p class="abs center venue">Held at CBD Courts (Wrenfold &amp; Harrowgate Clubs) and Elmhurst Uni. Sports &amp; Fitness<br>All finals will be at the Wrenfold Club</p>

  <div class="abs hero" role="img" aria-label="Two crossed squash racquets over a red, white and blue paint splash with stars"></div>

  <div class="abs bar-tab">
    <span class="amount">$3K</span>
    <span class="label">bar tab</span>
    <span class="desc">Saturday Night Open Bar in<br>CBD provided by Sponsor</span>
  </div>

  <div class="abs grades-box"></div>
  <h3 class="abs grades-title">GRADES AVAILABLE</h3>
  <ul class="abs grades-list col-a">
    <li>Mens and Ladies Squash Open, $14k in prizemoney</li>
    <li>Racquetball Open</li>
  </ul>
  <ul class="abs grades-list col-b">
    <li>Junior events</li>
    <li>All grades / abilities catered for Players guaranteed 3 matches <strong>$60 entry fee</strong></li>
  </ul>

  <p class="abs center weekday">Weekday matches also organised for CBD workers preferring to play during the day</p>
  <p class="abs center entries">Entries close 7th August 2021</p>

  <div class="abs contact">
    <div class="director">
      <span class="name">DANIEL MARSH</span>
      <span class="role">TOURNAMENT DIRECTOR</span>
    </div>
    <div class="details">
      <svg width="14" height="14" viewBox="0 0 14 14"><circle cx="7" cy="7" r="7" fill="var(--red)"/><path d="M4.5 3.5l1.5 0 .6 2-1 .8a5 5 0 0 0 2.1 2.1l.8-1 2 .6v1.5c0 .5-.5 1-1 1A6 6 0 0 1 3.5 4.5c0-.5.5-1 1-1z" fill="#fff"/></svg>
      <span>0400 555 019</span>
      <span class="divider"></span>
      <svg width="15" height="11" viewBox="0 0 15 11"><rect width="15" height="11" rx="1" fill="var(--red)"/><polyline points="1,1.5 7.5,6.5 14,1.5" fill="none" stroke="#fff" stroke-width="1.2"/></svg>
      <span>Daniel.Marsh@mailbox.net</span>
    </div>
  </div>

  <div class="abs partners">
    <span class="partner-name">Elmhurst Uni</span>
    <span class="partner-shape"></span>
    <span class="partner-shape square"></span>
    <span class="partner-name">WRENFOLD CLUB</span>
    <span class="partner-name">Harrowgate</span>
  </div>
</main>
</body>
</html>
```